Trade show post card for sportfishing

I would like a double sided postcard used to be a larger more descriptive, eye catching, marketing tool to be used at trade show. I want the double sided postcard to be descriptive and eye catching for both avid fisherman and inviting enough not to scare away first timers looking to enjoy the experience.

Target Market(s)

Males 25-60

Colors

Designer to choose colors to be used in the design.

Requirements
Must have
• My logo, website, phone number, type of trips, pictures of fishing trips we have had which I included below. But I do not need all of the pictures designers can use ones they feel will be most appealing
Nice to have
• Color scheme that works with my logo.

```html
<!DOCTYPE html>
<html lang="en">
<head>
<meta charset="utf-8">
<title>Hudson River Striped Bass Spring Postcard</title>
<link href="https://fonts.googleapis.com/css2?family=Oswald:wght@500;700&family=Open+Sans:wght@400;600;700&display=swap" rel="stylesheet">
<style>
  :root {
    --navy: #0f2f5a;
    --green: #4caf1f;
    --green-dark: #2f8a12;
    --white: #ffffff;
    --ink: #1d1d1d;
    --sky: #e4f1fa;
    --water: #4fb3e8;
    --stage: #eceff2;
    --line: #c9cfd6;
    --stamp: #e3e6ea;
  }
  * { box-sizing: border-box; margin: 0; padding: 0; }
  html, body { width: 820px; height: 1200px; overflow: hidden; }
  body { background: var(--stage); font-family: 'Open Sans', sans-serif; color: var(--ink); position: relative; }

  .card {
    position: absolute; left: 30px; width: 760px; height: 540px;
    background: var(--white); overflow: hidden;
    box-shadow: 0 4px 14px rgba(0,0,0,.18);
  }
  .card--front { top: 40px; background: linear-gradient(180deg, var(--sky) 0%, var(--white) 45%); }
  .card--back { top: 620px; }

  .shape-layer { position: absolute; inset: 0; }

  .water-band {
    position: absolute; left: 0; right: 0; bottom: 0; height: 80px;
    background: linear-gradient(180deg, rgba(79,179,232,0) 0%, rgba(79,179,232,.55) 55%, var(--water) 100%);
  }

  .headline {
    position: absolute; left: 24px; top: 26px;
    font-family: 'Oswald', sans-serif; font-weight: 700; color: var(--navy);
    font-size: 30px; line-height: 1.1; text-transform: uppercase;
  }
  .subhead {
    position: absolute; left: 24px; top: 98px;
    font-family: 'Oswald', sans-serif; font-weight: 500; color: var(--navy);
    font-size: 21px;
  }
  .subhead .season { color: var(--green); }

  .trip-list {
    position: absolute; left: 24px; top: 140px; width: 330px;
    background: var(--green); color: var(--white);
    padding: 16px 18px; list-style: none;
    font-size: 12.5px; line-height: 1.5;
  }
  .trip-list li { position: relative; padding-left: 14px; }
  .trip-list li + li { margin-top: 12px; }
  .trip-list li::before { content: ""; position: absolute; left: 0; top: 7px; width: 6px; height: 6px; background: var(--white); border-radius: 50%; }
  .trip-list .price { font-weight: 700; }

  .phone {
    position: absolute; display: flex; align-items: center; gap: 10px;
    font-family: 'Oswald', sans-serif; font-weight: 700; color: var(--navy);
  }
  .phone svg { flex: none; }
  .card--front .phone { left: 24px; top: 366px; font-size: 28px; }
  .card--back .phone { left: 22px; top: 376px; font-size: 30px; }

  .web-bar {
    position: absolute; background: var(--green); color: var(--white);
    font-weight: 600; display: flex; align-items: center;
  }
  .card--front .web-bar { left: 24px; top: 418px; width: 330px; height: 30px; border-radius: 15px; padding-left: 16px; font-size: 13.5px; }
  .card--back .web-bar {
    left: 0; top: 428px; width: 380px; height: 38px; padding-left: 22px; font-size: 16px;
    clip-path: polygon(0 0, 92% 0, 100% 50%, 92% 100%, 0 100%);
  }

  .brand-seal {
    position: absolute; left: 392px; top: 328px; width: 150px; height: 150px;
    border-radius: 50%; background: var(--white); border: 6px solid var(--green);
    display: flex; align-items: center; justify-content: center; text-align: center;
    font-family: 'Oswald', sans-serif; font-weight: 700; color: var(--green-dark);
    font-size: 22px; line-height: 1.1; text-transform: uppercase; padding: 16px;
  }

  .stamp-box { position: absolute; right: 40px; top: 34px; width: 64px; height: 76px; background: var(--stamp); }
  .address-lines { position: absolute; left: 460px; top: 250px; width: 260px; list-style: none; }
  .address-lines li { height: 36px; border-bottom: 1.5px solid var(--line); }
</style>
</head>
<body>

<section class="card card--front">
  <svg class="shape-layer" width="760" height="540" viewBox="0 0 760 540">
    <defs>
      <linearGradient id="catchGradient" x1="0" y1="0" x2="1" y2="1">
        <stop offset="0" stop-color="#9cc3de"/>
        <stop offset="0.5" stop-color="#6e8796"/>
        <stop offset="1" stop-color="#3c4a52"/>
      </linearGradient>
    </defs>
    <g role="img" aria-label="Photo of two anglers on a boat holding a large striped bass on the river">
      <circle cx="575" cy="260" r="235" fill="url(#catchGradient)"/>
    </g>
    <circle cx="575" cy="260" r="242" fill="none" stroke="var(--green)" stroke-width="12"/>
  </svg>
  <div class="water-band"></div>

  <h1 class="headline">Hudson River<br>Striped Bass Spring</h1>
  <p class="subhead">2018 Pricing <span class="season">(April &amp; May)</span></p>

  <ul class="trip-list">
    <li>Sunrise or Sunset trip, 5 hours with 1-4 guests, all live bait, top of the line fishing gear and electronics. <span class="price">$500.00</span></li>
    <li>Full day, 8 hours trip 1-4 guests, times selected by captain to provide best opportunity to catch fish, all live bait, top of the line fishing gear and electronics. <span class="price">$800.00</span></li>
  </ul>

  <p class="phone">
    <svg width="30" height="30" viewBox="0 0 30 30" aria-hidden="true"><circle cx="15" cy="15" r="13" fill="none" stroke="var(--navy)" stroke-width="2.4"/><path d="M10.5 8.5l2.4-.4 1.3 3-1.5 1.2a8 8 0 0 0 3.4 3.4l1.2-1.5 3 1.3-.4 2.4c-5.4.7-10.1-4-9.4-9.4z" fill="var(--navy)"/></svg>
    (555) 014-2290
  </p>
  <p class="web-bar">www.reelrivercharters.com</p>

  <div class="brand-seal">Reel River Charters</div>
</section>

<section class="card card--back">
  <svg class="shape-layer" width="760" height="540" viewBox="0 0 760 540">
    <defs>
      <linearGradient id="crewGradient" x1="0" y1="0" x2="1" y2="1">
        <stop offset="0" stop-color="#c9d3da"/>
        <stop offset="0.5" stop-color="#7d8a92"/>
        <stop offset="1" stop-color="#3f4a50"/>
      </linearGradient>
    </defs>
    <g role="img" aria-label="Photo of a group of anglers on a boat deck showing their catch of striped bass">
      <circle cx="130" cy="190" r="250" fill="url(#crewGradient)"/>
    </g>
    <circle cx="130" cy="190" r="257" fill="none" stroke="var(--green)" stroke-width="12"/>
    <rect x="0" y="360" width="400" height="180" fill="var(--white)"/>
  </svg>
  <div class="water-band"></div>

  <p class="phone">
    <svg width="32" height="32" viewBox="0 0 30 30" aria-hidden="true"><circle cx="15" cy="15" r="13" fill="none" stroke="var(--navy)" stroke-width="2.4"/><path d="M10.5 8.5l2.4-.4 1.3 3-1.5 1.2a8 8 0 0 0 3.4 3.4l1.2-1.5 3 1.3-.4 2.4c-5.4.7-10.1-4-9.4-9.4z" fill="var(--navy)"/></svg>
    (555) 014-2290
  </p>
  <p class="web-bar">www.reelrivercharters.com</p>

  <div class="stamp-box"></div>
  <ul class="address-lines"><li></li><li></li><li></li><li></li></ul>
</section>

</body>
</html>
```